Bref créative
Holloway & Daughters
Biz Card/Stationery
I need single sided standard sized Business Card [3.5" x 2"]
Spinnaker Font and what's in logo
Professional
Derek Fulton
Vice President, Operations
3172 W. Maple Boulevard
Indianapolis, IN
dfulton@hollowaydaughters.com
hollowaydaughters.com

```html
<!DOCTYPE html>
<html lang="en">
<head>
<meta charset="utf-8">
<title>Holloway &amp; Daughters — Business Card</title>
<link rel="stylesheet" href="https://fonts.googleapis.com/css2?family=Spinnaker&display=swap">
<style>
  :root {
    --backdrop: #e9e6e1;
    --card: #ffffff;
    --gold: #e0a526;
    --ink: #1b1b1b;
    --muted: #3a3a3a;
    --rule: #c9c9c9;
  }
  * { margin: 0; padding: 0; box-sizing: border-box; }
  html, body {
    width: 1200px; height: 914px; overflow: hidden;
    background: var(--backdrop);
    font-family: "Spinnaker", sans-serif;
  }
  .business-card {
    position: absolute; left: 75px; top: 157px;
    width: 1050px; height: 600px;
    background: var(--card);
    box-shadow: 0 10px 30px rgba(0,0,0,0.18);
    overflow: hidden;
  }
  .card-bands { position: absolute; inset: 0; }
  .brand {
    position: absolute; left: 60px; top: 150px; width: 440px;
    text-align: center;
  }
  .brand-mark {
    width: 70px; height: 70px; margin: 0 auto 22px;
    background: var(--ink);
  }
  .brand-name {
    color: var(--gold); font-size: 34px; letter-spacing: 2px;
    text-transform: uppercase; line-height: 1.1;
  }
  .brand-tagline {
    color: var(--ink); font-size: 17px; letter-spacing: 6px;
    text-transform: uppercase; margin-top: 6px;
  }
  .divider {
    position: absolute; left: 530px; top: 150px;
    width: 1px; height: 230px; background: var(--rule);
  }
  .contact {
    position: absolute; left: 556px; top: 150px; width: 460px;
    text-transform: uppercase; letter-spacing: 2px;
  }
  .contact-name { color: var(--gold); font-size: 24px; }
  .contact-title { color: var(--ink); font-size: 21px; line-height: 1.3; margin-top: 4px; }
  .contact-list { list-style: none; margin-top: 18px; }
  .contact-list li {
    display: flex; align-items: center; gap: 10px;
    color: var(--muted); font-size: 16px; line-height: 1.55;
  }
  .contact-list li.continued { padding-left: 26px; }
  .icon { width: 16px; height: 16px; flex: none; }
</style>
</head>
<body>
  <main class="business-card">
    <svg class="card-bands" width="1050" height="600" viewBox="0 0 1050 600" aria-hidden="true">
      <polygon points="0,430 575,430 540,478 0,478" fill="var(--gold)"/>
      <polygon points="835,478 1050,478 1050,530 800,530" fill="var(--ink)"/>
    </svg>

    <section class="brand">
      <div class="brand-mark"></div>
      <div class="brand-name">Holloway &amp; Daughters</div>
      <div class="brand-tagline">Construction Group</div>
    </section>

    <div class="divider"></div>

    <section class="contact">
      <div class="contact-name">Derek Fulton</div>
      <div class="contact-title">Vice President,<br>Operations</div>
      <ul class="contact-list">
        <li>
          <svg class="icon" viewBox="0 0 16 16"><circle cx="8" cy="8" r="8" fill="var(--gold)"/><path d="M8 3.5a2.8 2.8 0 0 0-2.8 2.8c0 2 2.8 5.2 2.8 5.2s2.8-3.2 2.8-5.2A2.8 2.8 0 0 0 8 3.5zm0 3.9a1.1 1.1 0 1 1 0-2.2 1.1 1.1 0 0 1 0 2.2z" fill="#fff"/></svg>
          3172 W. Maple Boulevard
        </li>
        <li class="continued">Indianapolis, IN</li>
        <li>
          <svg class="icon" viewBox="0 0 16 16"><circle cx="8" cy="8" r="8" fill="var(--gold)"/><path d="M5.4 4.2l1.3-.3.8 1.9-.9.7a5 5 0 0 0 2.9 2.9l.7-.9 1.9.8-.3 1.3c-3.6.3-6.7-2.8-6.4-6.4z" fill="#fff"/></svg>
          317-555-0142
        </li>
        <li>
          <svg class="icon" viewBox="0 0 16 16"><circle cx="8" cy="8" r="8" fill="var(--gold)"/><rect x="4" y="5" width="8" height="6" fill="#fff"/><path d="M4 5l4 3.2L12 5" stroke="var(--gold)" stroke-width="1" fill="none"/></svg>
          dfulton@hollowaydaughters.com
        </li>
        <li>
          <svg class="icon" viewBox="0 0 16 16"><circle cx="8" cy="8" r="8" fill="var(--gold)"/><circle cx="8" cy="8" r="4" stroke="#fff" stroke-width="1.2" fill="none"/><path d="M4 8h8M8 4c-1.6 2.4-1.6 5.6 0 8M8 4c1.6 2.4 1.6 5.6 0 8" stroke="#fff" stroke-width="0.9" fill="none"/></svg>
          hollowaydaughters.com
        </li>
      </ul>
    </section>
  </main>
</body>
</html>
```